Business Cards for Lean-In-Wise

I need a business card that uses elements of my color pallet and book along with my company name and logo. The primary thing I'd like to have stand out is the word Lean-In-Wise (i'd like to see this word in the orange from my pallet)
On the back of the card I want it to say Stop being Accountable, Be Lean-In-Wise

Contact Information for Business Card

Summit Hearthgroup logo, Lean-In-Wise, email - rtm@summithearthgroup.example, phone 555-208-4917, Harborview | Lakemont

Requirements
Nice to have
• colors from my color pallet

```html
<!DOCTYPE html>
<html lang="en">
<head>
<meta charset="utf-8">
<title>Lean-In-Wise Business Cards</title>
<link rel="stylesheet" href="https://fonts.googleapis.com/css2?family=Bebas+Neue&family=Montserrat:wght@400;500;600&display=swap">
<style>
  :root {
    --backdrop: #2a2a2c;
    --paper: #eeeeee;
    --orange: #e0562a;
    --navy: #1f2768;
    --navy-light: #2a3b8f;
    --brand-blue: #2f8fd8;
    --partner-blue: #1d4fa8;
    --partner-green: #4a9a3a;
    --white: #ffffff;
  }
  * { margin: 0; padding: 0; box-sizing: border-box; }
  html, body { width: 1200px; height: 800px; overflow: hidden; }
  body {
    background: var(--backdrop);
    position: relative;
    font-family: "Montserrat", sans-serif;
  }
  .card {
    position: absolute;
    left: 310px;
    width: 580px;
    height: 330px;
    overflow: hidden;
    background: var(--paper);
  }
  .card-front { top: 50px; }
  .card-back { top: 420px; }

  /* Front */
  .front-header {
    height: 100px;
    display: flex;
    align-items: center;
    justify-content: space-between;
    padding: 0 28px 0 34px;
  }
  .headline {
    font-family: "Bebas Neue", sans-serif;
    font-weight: 400;
    font-size: 86px;
    line-height: 1;
    color: var(--orange);
    padding-top: 8px;
  }
  .partner {
    display: flex;
    align-items: center;
    gap: 6px;
    font-weight: 600;
    font-size: 15px;
    color: var(--partner-blue);
  }
  .partner-mark {
    width: 14px; height: 14px;
    background: var(--partner-green);
  }
  .front-body {
    height: 230px;
    background: linear-gradient(90deg, var(--navy) 0%, var(--navy-light) 100%);
    display: flex;
    align-items: center;
    padding: 0 30px 0 36px;
  }
  .brand {
    width: 230px;
    display: flex;
    flex-direction: column;
    align-items: flex-start;
    gap: 12px;
  }
  .brand-mark {
    width: 46px; height: 46px;
    border-radius: 50%;
    background: var(--brand-blue);
  }
  .brand-name {
    font-weight: 400;
    font-size: 24px;
    line-height: 1.15;
    color: var(--brand-blue);
  }
  .contact { color: var(--white); }
  .contact-name {
    font-weight: 600;
    font-size: 26px;
    letter-spacing: 0.5px;
    margin-bottom: 14px;
  }
  .contact-list { list-style: none; }
  .contact-list li {
    display: flex;
    align-items: center;
    gap: 10px;
    font-size: 14px;
    font-weight: 500;
    line-height: 24px;
  }
  .contact-list svg { width: 15px; height: 15px; flex: none; fill: var(--orange); }

  /* Back */
  .back-top {
    height: 200px;
    padding: 28px 0 0 30px;
    font-family: "Bebas Neue", sans-serif;
    color: var(--orange);
  }
  .stop { font-size: 112px; line-height: 0.95; }
  .accountable { font-size: 60px; line-height: 1; margin-top: -2px; }
  .back-band {
    height: 130px;
    background: var(--orange);
    display: flex;
    align-items: center;
    padding-left: 30px;
    font-family: "Bebas Neue", sans-serif;
    color: var(--white);
    gap: 14px;
  }
  .be { font-size: 64px; line-height: 1; padding-top: 18px; }
  .slogan-word { font-size: 104px; line-height: 1; padding-top: 8px; }
</style>
</head>
<body>

<section class="card card-front">
  <header class="front-header">
    <h1 class="headline">Lean-In-Wise</h1>
    <div class="partner"><span class="partner-mark"></span>Stepwise90</div>
  </header>
  <div class="front-body">
    <div class="brand">
      <span class="brand-mark"></span>
      <span class="brand-name">Summit<br>Hearthgroup</span>
    </div>
    <div class="contact">
      <p class="contact-name">Reid Marlow</p>
      <ul class="contact-list">
        <li><svg viewBox="0 0 16 16"><path d="M8 1 1 7.5h2V15h4v-4h2v4h4V7.5h2z"/></svg>Harborview | Lakemont</li>
        <li><svg viewBox="0 0 16 16"><path d="M3.6 1.5 6 4.2 4.7 6.1c.9 2 2.4 3.5 4.4 4.4l1.9-1.3 2.7 2.4-1.3 2.4C7.6 13.9 2.1 8.4 1.2 2.8z"/></svg>555-208-4917</li>
        <li><svg viewBox="0 0 16 16"><path d="M1 3h14v10H1zM2 4.2v.4l6 4.2 6-4.2v-.4z"/></svg>rtm@summithearthgroup.example</li>
        <li><svg viewBox="0 0 16 16"><path d="M8 1a7 7 0 1 0 0 14A7 7 0 0 0 8 1zm0 1.4c.8 0 1.8 1.9 2 4.6H6c.2-2.7 1.2-4.6 2-4.6zM2.5 7h2.2c.1-1.7.5-3.1 1-4A5.7 5.7 0 0 0 2.5 7zm8.8 0h2.2a5.7 5.7 0 0 0-3.2-4c.5.9.9 2.3 1 4zM2.5 9a5.7 5.7 0 0 0 3.2 4c-.5-.9-.9-2.3-1-4zm3.5 0c.2 2.7 1.2 4.6 2 4.6s1.8-1.9 2-4.6zm5.3 0c-.1 1.7-.5 3.1-1 4a5.7 5.7 0 0 0 3.2-4z"/></svg>www.summithearthgroup.example</li>
      </ul>
    </div>
  </div>
</section>

<section class="card card-back">
  <div class="back-top">
    <p class="stop">Stop</p>
    <p class="accountable">Being Accountable</p>
  </div>
  <div class="back-band">
    <span class="be">Be</span>
    <span class="slogan-word">Lean-In-Wise</span>
  </div>
</section>

</body>
</html>
```